Brochure Design Project -postcard size 1/4 of A4 sheet

We are a bright and happening cafe which is an old milk bar converted into a cafe. I need to have a postcard designed for letterbox drop to let locals know what great food and coffee we have. The postcard ideally would have a black and white old world milk bar scene and a promise of old fashion service in a changing neighborhood.
Here is a little about our place
http://www.nearbylist.com.au/business/carwell-lane-soda-shop/richmond
I can't seem to put any updates but if you are having trouble with image graphics are ok that depicts an "old world" coffee shoo from 60s or 70s postcard size is a 1/4 of an A4 sheet
http://www.friendspage.example/group.php?gid=51847260913&v=wall
I am working off an iPad and this website does not allow feedback via iPad so have to put everything in brief link to a Facebook site now
Updates
Yeyyy !! I have been working off an Ipad which does not allow me to give feedback. I love the old world look of the recent designs I have now attached our logo and a facebook site of the cafe for more details.
Many Thanks
Marl a
Target Market(s)
Local community aged mainly 20 to 50
Industry/Entity Type
Fashion
Requirements
Must have
- Black and white image on the front of postcard an old milk bar scene and the words
Carwell lane soda shop ....a constant among change
Nice to have
- On the back to read we need to know what you want at your local foodstore
A little about our milk bar can be read at

```html
<!DOCTYPE html>
<html lang="en">
<head>
<meta charset="utf-8">
<title>Carwell Lane Soda Shop – Postcard Back</title>
<link rel="stylesheet" href="https://fonts.googleapis.com/css2?family=Crimson+Text:wght@700&display=swap">
<style>
  :root {
    --paper: #ffffff;
    --paper-soft: #f2f2f2;
    --paper-edge: #9a9a9a;
    --ink: #141414;
    --rule: #b6b6b6;
  }
  html, body {
    margin: 0;
    padding: 0;
    overflow: hidden;
    background: var(--paper);
  }
  .postcard-back {
    position: relative;
    width: 1200px;
    height: 856px;
    overflow: hidden;
    background:
      radial-gradient(ellipse 80% 78% at 50% 50%, var(--paper) 60%, var(--paper-soft) 78%, var(--paper-edge) 100%);
    box-shadow: inset 0 0 90px 10px rgba(0, 0, 0, 0.22);
  }
  .paper-grain {
    position: absolute;
    inset: 0;
    width: 1200px;
    height: 856px;
    pointer-events: none;
  }
  .intro-copy {
    position: absolute;
    left: 86px;
    top: 199px;
    width: 520px;
    margin: 0;
    font-family: "Crimson Text", Georgia, serif;
    font-weight: 700;
    font-size: 26px;
    line-height: 34.3px;
    letter-spacing: 0.5px;
    color: var(--ink);
    white-space: nowrap;
  }
  .intro-copy p {
    margin: 0 0 34.3px;
  }
  .divider {
    position: absolute;
    left: 597px;
    top: 176px;
    width: 3px;
    height: 542px;
    background: var(--rule);
  }
  .address-lines {
    position: absolute;
    left: 646px;
    top: 0;
    width: 492px;
    height: 856px;
  }
  .address-line {
    position: absolute;
    left: 0;
    width: 100%;
    height: 3px;
    background: var(--rule);
  }
  .address-line:nth-child(1) { top: 283px; }
  .address-line:nth-child(2) { top: 394px; }
  .address-line:nth-child(3) { top: 505px; }
  .address-line:nth-child(4) { top: 622px; }
</style>
</head>
<body>
  <main class="postcard-back">
    <svg class="paper-grain" viewBox="0 0 1200 856" aria-hidden="true">
      <defs>
        <filter id="grain">
          <feTurbulence type="fractalNoise" baseFrequency="0.9 0.05" numOctaves="3" seed="7"/>
          <feColorMatrix values="0 0 0 0 0.35  0 0 0 0 0.35  0 0 0 0 0.35  0 0 0 -1.6 1.1"/>
        </filter>
        <radialGradient id="edge-fade" cx="50%" cy="50%" r="60%">
          <stop offset="0.62" stop-color="#000"/>
          <stop offset="1" stop-color="#fff"/>
        </radialGradient>
        <mask id="edge-mask">
          <rect width="1200" height="856" fill="url(#edge-fade)"/>
        </mask>
      </defs>
      <rect width="1200" height="856" filter="url(#grain)" mask="url(#edge-mask)" opacity="0.55"/>
    </svg>
    <section class="intro-copy">
      <p>Carwell Lane Soda Shop was once a<br>
      traditional milk bar and is now a hip<br>
      cafe serving hearty breakfasts and a<br>
      casual lunch menu.<br>
      Ii is ideal location for a casual catch<br>
      up with friends or a working lunch.</p>
      <p>We're also kid friendly and have a<br>
      couple of long 8 seater tables - ideal<br>
      for the big extended family breakfast<br>
      or lunch.</p>
      <p>We're located opposite Harbourline Studios<br>
      with plenty of on street parking.</p>
    </section>
    <div class="divider"></div>
    <div class="address-lines">
      <div class="address-line"></div>
      <div class="address-line"></div>
      <div class="address-line"></div>
      <div class="address-line"></div>
    </div>
  </main>
</body>
</html>
```